店舗は車通りの多い道路の交差点に面しております※添付ファイル参照
歩行者よりも車から見られることが圧倒的に多いのでパッと見で花屋であることがわかるようなデザインを希望しております
写真では壁面が凹凸しているのが分かると思いますが赤く囲ったところに平らなプレートを貼り付け、そこにデザインされたものを出力します、既存のロゴ等は全て取り外します※添付ファイル参照
看板には 花 の一文字を入れて下さい、店名は必要ありません
看板サイズ:横 210cm×縦 680cm
ピンクメイン

カラーがイメージにピッタリで、デザインも写真を使わずイラストで仕上がっており一つ一つの模様も大きいため全体がハッキリとしているのでインパクトもある
色・デザイン共に建物のとのフィーリングが良いと判断しました

長期間において多数のご提案ありがとうございました、こんなに多くのエントリーをいただけるとは思っていなかったので正直ビックリしております、おかげで当選作品を選ぶのに一週間もかかってしまいました、こちらとしてはうれしい限りです。
ただ今回当選させられなかった方々には申し訳なく思います、また次の機会ありましたらなにとぞよろしくお願いします。

```html
<!DOCTYPE html>
<html lang="ja">
<head>
<meta charset="utf-8">
<title>花 FLOWER SHOP 看板</title>
<link rel="stylesheet" href="https://fonts.googleapis.com/css2?family=Archivo+Black&family=Noto+Sans+JP:wght@900&display=swap">
<style>
  :root {
    --page: #ffffff;
    --red: #e5202e;
    --pink-bg: #f6c7dc;
    --pink-ink: #e8679f;
    --pink-ink-soft: #ea7db0;
    --green: #6dbf86;
    --white: #ffffff;
  }
  html, body {
    margin: 0;
    padding: 0;
    width: 1200px;
    height: 2688px;
    overflow: hidden;
    background: var(--page);
  }
  .sign {
    position: absolute;
    left: 168px;
    top: 188px;
    width: 840px;
    height: 2372px;
  }
  .sign__kanji-panel {
    position: absolute;
    left: 0;
    top: 0;
    width: 840px;
    height: 652px;
    background: var(--red);
    display: flex;
    align-items: center;
    justify-content: center;
  }
  .sign__kanji {
    font-family: "Noto Sans JP", sans-serif;
    font-weight: 900;
    font-size: 500px;
    line-height: 1;
    color: var(--white);
    margin-top: -10px;
  }
  .sign__body {
    position: absolute;
    left: 0;
    top: 652px;
    width: 840px;
    height: 1488px;
    background: var(--pink-bg);
    overflow: hidden;
  }
  .sign__word {
    position: absolute;
    font-family: "Archivo Black", sans-serif;
    writing-mode: vertical-rl;
    text-orientation: sideways;
    line-height: 1;
    margin: 0;
    white-space: nowrap;
  }
  .sign__word--flower {
    left: 488px;
    top: 40px;
    font-size: 300px;
    letter-spacing: -4px;
    color: var(--pink-ink);
  }
  .sign__word--shop {
    left: 62px;
    top: 40px;
    font-size: 300px;
    letter-spacing: -4px;
    color: var(--pink-ink-soft);
  }
  .sign__rose {
    position: absolute;
    left: 64px;
    top: 1196px;
    width: 290px;
    height: 280px;
  }
  .sign__base {
    position: absolute;
    left: 0;
    top: 2140px;
    width: 840px;
    height: 232px;
    background: var(--green);
  }
</style>
</head>
<body>
  <div class="sign">
    <div class="sign__kanji-panel">
      <span class="sign__kanji">花</span>
    </div>
    <div class="sign__body">
      <p class="sign__word sign__word--flower">FLOWER</p>
      <p class="sign__word sign__word--shop">SHOP</p>
      <svg class="sign__rose" viewBox="0 0 290 280" role="img" aria-label="バラの花と葉のイラスト">
        <defs>
          <radialGradient id="rose-tone" cx="50%" cy="40%" r="60%">
            <stop offset="0%" stop-color="#f3a3c6"/>
            <stop offset="100%" stop-color="#e97fb0"/>
          </radialGradient>
        </defs>
        <ellipse cx="150" cy="130" rx="125" ry="115" fill="url(#rose-tone)"/>
      </svg>
    </div>
    <div class="sign__base"></div>
  </div>
</body>
</html>
```